Single Sided 1 Page Tour Flyer in the same theme as previous brochure

We need a single sided 8.5 x 11 flyer in the same theme and color scheme as the previous brochure we worked on together. the flyer should include the following

1. company logo up top (just like on the front panel of previous brochure
2. tour name "Silver Meadow Trail Loop" also on the top
3. a large photo towards the top of the flyer, similar to the brochure front
4. 3 panels of text: left one for tour prices, whats included, additional notes, center and right panels for tour program details (day 1, day 2, etc)
5. below that, a few lines for additional details, like small print and stuff
6. company address, phone numbers, email address, and website link
6. below that a banner of small photos, maybe 4 in a row, similar to the brochure

details of the actual tour can be found at this link:
http://bluefernvoyage.ru/en/tours/silver-meadow-trail-loop-11-days/

once again, we would love for the flyer to be in the same theme and style as the other brochure, so it matches, we loved the previous work!!

```html
<!DOCTYPE html>
<html lang="en">
<head>
<meta charset="utf-8">
<title>Silver Meadow Trail Loop – BlueFern Voyage</title>
<link rel="stylesheet" href="https://fonts.googleapis.com/css2?family=Signika:wght@400;600;700&family=Questrial&display=swap">
<style>
:root{
  --red:#c8141e;
  --red-dark:#9e0d15;
  --gold:#f2c21b;
  --ink:#2b2b2b;
  --text:#3a3a3a;
  --muted:#6a6a6a;
  --footer:#333436;
  --white:#ffffff;
}
*{margin:0;padding:0;box-sizing:border-box}
html,body{width:949px;height:1200px;overflow:hidden;background:var(--white)}
body{position:relative;font-family:"Questrial",sans-serif;color:var(--text)}
.shapes{position:absolute;inset:0}
.abs{position:absolute}

.brand{left:44px;top:88px;display:flex;align-items:center;gap:12px}
.brand-dot{width:40px;height:40px;border-radius:50%;background:var(--gold)}
.brand-name{font-family:"Signika",sans-serif;font-weight:600;font-size:34px;color:var(--ink);letter-spacing:-.5px}
.tour-title{right:36px;top:72px;font-family:"Signika",sans-serif;font-weight:700;font-size:35px;color:var(--ink)}

.itinerary-head{left:40px;top:502px;display:flex;align-items:center;gap:8px;font-family:"Signika",sans-serif;font-weight:700;font-size:26px;color:var(--ink)}
.itinerary-head i{display:block;width:14px;height:14px;border-radius:50%;background:var(--gold)}
.cities{left:297px;top:502px;width:420px;font-family:"Signika",sans-serif;font-weight:600;font-size:17.5px;line-height:22px;color:var(--red)}

.badge{left:752px;top:468px;width:154px;height:96px;text-align:center;color:#ffd9d9;font-size:13px;line-height:16px;padding-top:14px}
.badge strong{display:block;font-family:"Signika",sans-serif;font-weight:700;font-size:27px;line-height:32px;color:var(--gold)}

.prices-col{left:40px;top:546px;width:282px;font-size:13px;line-height:17px}
.prices{display:flex;gap:34px;margin:14px 0 18px}
.prices dt{font-family:"Signika",sans-serif;font-weight:700;font-size:17px;color:var(--ink)}
.prices dd{font-family:"Signika",sans-serif;font-weight:600;font-size:18px;color:var(--red);margin-top:4px}
.list-title{font-family:"Signika",sans-serif;font-weight:600;font-size:13.5px;color:var(--ink);margin-bottom:2px}
.bullets{list-style:none;margin-bottom:14px}
.bullets li{padding-left:9px;position:relative}
.bullets li::before{content:"";position:absolute;left:0;top:6px;width:5px;height:5px;border-radius:50%;background:var(--red)}
.note{font-style:italic;font-size:12.8px;line-height:15.8px;text-align:justify;margin-bottom:7px}
.note:first-of-type{margin-top:10px}

.day-col{width:265px;font-size:12.8px;line-height:15.8px;text-align:justify}
.day-col.mid{left:345px;top:558px}
.day-col.right{left:644px;top:558px;width:272px}
.day{margin-bottom:16px}
.day h3{font-family:"Signika",sans-serif;font-weight:600;font-size:15.5px;color:var(--red);margin-bottom:2px}
.day em{font-style:italic}

.fineprint{left:414px;top:1040px;width:512px;font-size:9.4px;line-height:11px;font-style:italic;color:var(--muted)}
.fineprint p{margin-bottom:5px}
.fine-dot{left:352px;top:1040px;width:44px;height:44px;border-radius:50%;background:var(--gold)}

.contact{color:var(--white);display:flex;align-items:center;gap:7px}
.phone{left:62px;top:1112px;font-family:"Signika",sans-serif;font-weight:600;font-size:20px}
.address{left:66px;top:1142px;font-size:14px;line-height:18px;align-items:flex-start}
.email{left:350px;top:1164px;font-size:17px}
.web{left:666px;top:1164px;font-size:17px}
</style>
</head>
<body>

<svg class="shapes" width="949" height="1200" viewBox="0 0 949 1200">
  <defs>
    <linearGradient id="topShade" x1="0" y1="0" x2="1" y2="0">
      <stop offset="0" stop-color="#ffffff"/>
      <stop offset="1" stop-color="#ececec"/>
    </linearGradient>
    <linearGradient id="bridge" x1="0" y1="0" x2="0" y2="1">
      <stop offset="0" stop-color="#4a4c8c"/>
      <stop offset=".45" stop-color="#7a6aa6"/>
      <stop offset=".7" stop-color="#c06a3a"/>
      <stop offset="1" stop-color="#3a3056"/>
    </linearGradient>
    <linearGradient id="statue" x1="0" y1="0" x2="0" y2="1"><stop offset="0" stop-color="#e8eef2"/><stop offset="1" stop-color="#6f8f82"/></linearGradient>
    <linearGradient id="street" x1="0" y1="0" x2="0" y2="1"><stop offset="0" stop-color="#8c8f86"/><stop offset="1" stop-color="#4d5150"/></linearGradient>
    <linearGradient id="night" x1="0" y1="0" x2="0" y2="1"><stop offset="0" stop-color="#1d2a66"/><stop offset="1" stop-color="#5d5a60"/></linearGradient>
    <linearGradient id="falls" x1="0" y1="0" x2="0" y2="1"><stop offset="0" stop-color="#6f9fd0"/><stop offset=".5" stop-color="#e6eef2"/><stop offset="1" stop-color="#3e6f80"/></linearGradient>
    <linearGradient id="badgeFill" x1="0" y1="0" x2="0" y2="1"><stop offset="0" stop-color="#d81c25"/><stop offset="1" stop-color="#9e0d15"/></linearGradient>
  </defs>

  <path d="M0 0H949V190C760 150 560 90 330 110 180 122 60 150 0 170Z" fill="url(#topShade)"/>
  <path d="M40 205C250 168 520 160 949 190V198C520 170 250 178 40 212Z" fill="var(--gold)"/>

  <path d="M40 200C250 180 500 176 620 180L620 480C420 470 200 470 40 478Z" fill="url(#bridge)" role="img" aria-label="Night photo of a lit suspension bridge over a bay with a city skyline"/>
  <path d="M600 180C760 182 880 188 949 198V462C800 478 650 482 560 482 610 420 600 300 640 250 650 230 620 200 600 180Z" fill="var(--red)"/>
  <path d="M610 484C760 470 880 460 949 452V462C880 470 760 480 610 490Z" fill="var(--gold)"/>

  <ellipse cx="613" cy="243" rx="100" ry="60" fill="url(#statue)" role="img" aria-label="Photo of a green copper statue crown against the sky"/>
  <ellipse cx="822" cy="243" rx="100" ry="60" fill="url(#street)" role="img" aria-label="Photo of street signs on a city corner"/>
  <ellipse cx="613" cy="394" rx="100" ry="60" fill="url(#night)" role="img" aria-label="Photo of a lit hotel street at night"/>
  <ellipse cx="822" cy="394" rx="100" ry="60" fill="url(#falls)" role="img" aria-label="Photo of a boat below a large waterfall"/>
  <circle cx="717" cy="318" r="13" fill="var(--gold)"/>

  <ellipse cx="829" cy="515" rx="78" ry="49" fill="url(#badgeFill)" stroke="#b0111a" stroke-width="2"/>

  <path d="M0 1080C180 1050 360 1080 470 1128 530 1150 580 1158 650 1158L610 1200H0Z" fill="var(--footer)"/>
  <path d="M0 1080C180 1050 360 1080 470 1128 530 1150 580 1158 650 1158" fill="none" stroke="#9a9a9a" stroke-width="3"/>
  <path d="M672 1150C780 1132 880 1120 949 1114V1200H622Z" fill="var(--red)"/>
</svg>

<div class="abs brand"><span class="brand-dot"></span><span class="brand-name">BlueFern Voyage</span></div>
<h1 class="abs tour-title">Silver Meadow Trail Loop</h1>

<h2 class="abs itinerary-head"><i></i>Tour Itinerary<i></i></h2>
<p class="abs cities">New York, Washington, D.C., Philadelphia, Boston, Montreal, Quebec, Ottawa, Niagara Falls</p>
<div class="abs badge">Cost for<br>1 person from<strong>$1,495</strong></div>

<section class="abs prices-col">
  <p>The cost of tour for one person<br><em>(Personalize in process of purchasing)</em></p>
  <dl class="prices">
    <div><dt>DBL</dt><dd>$1,495</dd></div>
    <div><dt>SNGL</dt><dd>$1,995</dd></div>
    <div><dt>TRPL</dt><dd>$1,395</dd></div>
  </dl>
  <p class="list-title">Included in Price:</p>
  <ul class="bullets">
    <li>Double occupancy in hotels along the route</li>
    <li>Breakfasts</li>
    <li>Excursions as per itinerary</li>
  </ul>
  <p class="list-title">Not Included in Price:</p>
  <ul class="bullets">
    <li>Domestic airfare</li>
    <li>Tips for the driver and guide</li>
  </ul>
  <p class="note">*Departure from Buffalo Airport (BUF) is also possible (transfer is not included in the program, and is an additional charge)</p>
  <p class="note">Participants can also return to New York, Manhattan, or JFK Airport (transfer is free). Departure from JFK airport is not possible on the 11th Day due to time constraints.</p>
  <p class="note">*We recommend extending your trip with additional nights in New York, for leisure time in Manhattan, Broadway shows, shopping, and much more.</p>
</section>

<section class="abs day-col mid">
  <div class="day"><h3>Day 1</h3><p>Arrival to Washington, D.C., registration in hotel. Overnight in Washington, D.C.</p></div>
  <div class="day"><h3>Day 2</h3><p>Sightseeing tour of Washington, D.C.: memorials, Capitol Building, White House, museums, and much more. Overnight in Washington, D.C.</p></div>
  <div class="day"><h3>Day 3</h3><p>Departure to Philadelphia. Sightseeing tour of Philadelphia. Departure to New York, leisure time in the evening. Overnight in New York</p></div>
  <div class="day"><h3>Day 4</h3><p>Sightseeing tour of New York: Manhattan, Wall Street, United Nations Building, Broadway, Times Square. <em>*optional cruise to the Statue of Liberty and Ellis Island. Overnight in New York</em></p></div>
  <div class="day"><h3>Day 5</h3><p>Departure to Boston. Sightseeing tour of Boston, Harvard University. Overnight in Boston</p></div>
</section>

<section class="abs day-col right">
  <div class="day"><h3>Day 6</h3><p>Departure to Montreal, sightseeing tour of the city. Overnight in Montreal</p></div>
  <div class="day"><h3>Day 7</h3><p>Sightseeing tour of Quebec, return to Montreal. Overnight in Montreal</p></div>
  <div class="day"><h3>Day 8</h3><p>Second part of sightseeing tour of Montreal. Old Town, Montreal Port, Notre Dame de Montreal. Departure to Ottawa, sightseeing tour of Ottawa. Overnight in Ottawa</p></div>
  <div class="day"><h3>Day 9</h3><p>Departure to Rockport, cruise of 1,000 Islands, Departure to Toronto. Overnight in Toronto</p></div>
  <div class="day"><h3>Day 10</h3><p>Sightseeing tour of Toronto. Departure to Niagara Falls. Cruise to the Niagara Falls. Overnight in Niagara Falls</p></div>
  <div class="day"><h3>Day 11</h3><p>Transfer to Toronto Airport (YYZ). End of tour program</p></div>
</section>

<div class="abs fine-dot"></div>
<div class="abs fineprint">
  <p>**order of sights of interest may change with advance notice</p>
  <p>* BlueFern Voyage, Inc. cannot be held liable for complications arising from improperly filled out forms, passports or visas, especially upon crossing international borders.</p>
  <p>* BlueFern Voyage, Inc. cannot be held liable for forgotten personal belongings left in hotels, aboard the bus, or lost throughout the duration of the tour.</p>
</div>

<div class="abs contact phone">
  <svg width="20" height="20" viewBox="0 0 20 20"><circle cx="10" cy="10" r="9" fill="none" stroke="var(--gold)" stroke-width="1.6"/><path d="M7 5.5l2 2-1 1.3c.6 1.3 1.5 2.2 2.8 2.8l1.3-1 2 2-1.2 1.4c-3.2-.4-6.3-3.5-6.7-6.7Z" fill="var(--gold)"/></svg>
  +1 (800) 555-0142
</div>
<div class="abs contact address">
  <svg width="12" height="16" viewBox="0 0 12 16"><path d="M6 0a6 6 0 0 1 6 6c0 4-6 10-6 10S0 10 0 6a6 6 0 0 1 6-6Z" fill="var(--gold)"/><circle cx="6" cy="6" r="2.2" fill="var(--footer)"/></svg>
  <span>4100 Harbor View Ave. Suite #310<br>Glendale, CA 91203</span>
</div>
<div class="abs contact email">
  <svg width="18" height="13" viewBox="0 0 18 13"><rect x="1" y="1" width="16" height="11" fill="none" stroke="var(--gold)" stroke-width="1.6"/><path d="M1 1l8 6 8-6" fill="none" stroke="var(--gold)" stroke-width="1.6"/></svg>
  info@bluefernvoyage.com
</div>
<div class="abs contact web">
  <svg width="15" height="15" viewBox="0 0 16 16"><circle cx="8" cy="8" r="7" fill="none" stroke="var(--gold)" stroke-width="1.5"/><ellipse cx="8" cy="8" rx="3" ry="7" fill="none" stroke="var(--gold)" stroke-width="1.2"/><path d="M1 8h14" stroke="var(--gold)" stroke-width="1.2"/></svg>
  www.bluefernvoyage.com
</div>

</body>
</html>
```